Postcard Design

Looking for 4.25 x6 postcard design for mass mailing
Design should be eye catching, energetic and draw the viewer in

Data for postcard to include:
Logo and slogan
Pediatric Occupational, Physical and Speech Therapy Services; Assistive Technology Evaluation and Training

Speech-Language Therapy
oral motor skills
speech delays
language skills
Articulation
Voice
fluency
cognitive skills
feeding disorders
Play skills

OCCUPATIONAL THERAPY
Our occupational therapists use play in therapy to help your child develop the skills he/she needs to perform their job of living and playing, including but not limited to:
- Increasing independence in self-care skills such as feeding, dressing and grooming
- Improving developmental skills such as rolling, sitting, standing
- Improving their sensory processing, balance, coordination and motor planning
- Difficulty tolerating clothing
- Poor balance - doesn't ride a bike/climb on slides, falls frequently, cries when moved unexpectedly
- Intolerance to textures/odors/loud sounds/movement
- Delayed handwriting and fine motor skills and/or
avoids fine motor activities such as using crayons, fasteners on clothing, pencils
- Limited diet-refuses to try new foods, gags when trying new tastes, textures
- Appears extremely anxious, states frequent fears of harmless things

CONTACT US TODAY for a FREE 15 minute consultation/Screen
(301) 555-4182
info@brightwillowkids.example
www.brightwillowkids.example

Physical therapy
Delayed crawling / walking
Persistent toe walking habits
Poor unsupported sitting/standing balance
Trouble learning how to jump, skip, ride a bike
Decreased ability to throw and catch a ball
Delayed motor milestones
Need for wheelchair mobility training
Balance coordination and motor planning difficulty
Strength , muscle tone and/ R range of motion impairment
Sports injuries
Postural control and positioning difficulty

```html
<!DOCTYPE html>
<html lang="en">
<head>
<meta charset="utf-8">
<title>Bright Willow Kids – Postcard</title>
<link rel="stylesheet" href="https://fonts.googleapis.com/css2?family=Open+Sans:ital,wght@0,400;0,600;0,700;1,400&family=Oswald:wght@500&display=swap">
<style>
:root{
  --blue:#0b72c6;
  --deep-blue:#0d68b8;
  --teal:#00a49b;
  --teal-light:#7fd0c8;
  --gold:#f4d56a;
  --orange:#e6a65b;
  --ink:#2b2b2b;
  --white:#ffffff;
  --mist:#f3f5f7;
  --page:#5e5f61;
  --line:#6e6e6e;
}
*{box-sizing:border-box;margin:0;padding:0}
html,body{width:900px;height:1200px;overflow:hidden}
body{background:var(--page);font-family:"Open Sans",Arial,sans-serif;position:relative}
.card{position:absolute;background:var(--white);overflow:hidden}
.card-bg{position:absolute;inset:0;width:100%;height:100%}
.abs{position:absolute}
ul{list-style:none}

/* ticks */
.ticks li{position:relative;padding-left:11px}
.ticks li::before,.tick-item::before{content:"";position:absolute;left:0;top:4px;width:7px;height:7px;border:1px solid currentColor;border-radius:50%}
.ticks li::after,.tick-item::after{content:"";position:absolute;left:2.6px;top:5.2px;width:2px;height:3.5px;border:solid currentColor;border-width:0 1px 1px 0;transform:rotate(45deg)}

/* ---------- front ---------- */
.front{left:113px;top:94px;width:674px;height:476px}
.brand{left:31px;top:26px;display:flex;align-items:center;gap:10px}
.brand-dot{width:40px;height:40px;border-radius:50%;background:var(--teal)}
.brand-name{font-weight:700;font-size:20px;color:var(--deep-blue);line-height:1}
.brand-slogan{left:86px;top:70px;font-style:italic;font-size:9px;color:var(--deep-blue)}
.site-top{left:388px;top:16px;color:var(--white);font-size:12.5px;letter-spacing:.6px;display:flex;align-items:center;gap:7px;white-space:nowrap}
.site-top b{font-weight:600}
.photo-forest{left:312px;top:43px;width:362px;height:172px;
  background:linear-gradient(180deg,#b8c6b4 0%,#8fae74 45%,#5d9a33 100%);
  clip-path:polygon(11.6% 0,100% 0,100% 100%,24.9% 100%,0 27.3%)}
.services{left:31px;top:106px}
.services li{font-family:"Oswald","Arial Narrow",sans-serif;font-weight:500;font-size:18.5px;color:var(--deep-blue);line-height:29.5px;display:flex;align-items:center;gap:9px;letter-spacing:-.1px}
.services li::before{content:"";width:10px;height:10px;border-radius:50%;background:var(--teal);flex:none}
.pill{left:181px;top:200px;width:312px;height:30px;border-radius:15px;
  background:linear-gradient(90deg,var(--gold),var(--orange));
  color:var(--white);font-weight:700;font-size:19px;letter-spacing:.5px;
  display:flex;align-items:center;justify-content:center}
.ot-intro{left:32px;width:610px;top:237px;text-align:center;color:var(--white);font-size:12.4px;line-height:17.5px}
.rule-front{left:31px;top:276px;width:612px;height:1px;background:rgba(255,255,255,.85)}
.ot-list{color:var(--white);font-size:9.7px;line-height:13.8px;top:283px;letter-spacing:-.05px}
.ot-list li{margin-bottom:1.6px}
.ot-left{left:31px;width:324px}
.ot-right{left:370px;width:292px}
.divider-dots{left:361px;top:284px;height:111px;border-left:1px dotted rgba(255,255,255,.8)}
.cta-bar{left:34px;top:409px;width:606px;height:29px;
  background:linear-gradient(90deg,var(--gold),var(--orange));
  color:var(--white);font-family:"Oswald","Arial Narrow",sans-serif;font-weight:500;font-size:21px;
  letter-spacing:.35px;display:flex;align-items:center;justify-content:center;white-space:nowrap}
.contact-row{left:34px;top:440px;height:30px;width:620px;display:flex;align-items:center;color:var(--white);font-weight:700;font-size:21px;white-space:nowrap}
.contact-row .sep{width:1px;height:18px;background:var(--white);margin:0 22px 0 32px}
.contact-row svg{flex:none;margin-right:9px}

/* ---------- back ---------- */
.back{left:111px;top:635px;width:678px;height:480px}
.back h2{position:absolute;font-weight:700;font-size:20.5px;letter-spacing:.2px;color:var(--white);line-height:1}
.h-speech{left:29px;top:24px}
.h-physical{left:29px;top:117px}
.back .h-contact{left:29px;top:367px;color:var(--ink)}
.back-rule{height:1px;background:var(--white)}
.speech-list{left:29px;top:55px;display:grid;grid-template-columns:123px 88px auto;row-gap:1px;color:var(--white);font-size:11.6px;line-height:16.6px}
.back .ticks li{padding-left:15px}
.pt-list{left:29px;top:158px;width:440px;color:var(--white);font-size:11.6px;line-height:15.2px}
.pt-list li{margin-bottom:1.7px}
.pt-list li:first-child{margin-bottom:4px}
.pt-list .col2{position:absolute;left:164px;top:0;padding-left:13px;white-space:nowrap}
.photo-student{left:249px;top:276px}
.stamp{left:577px;top:34px;width:66px;height:69px;border:1px solid var(--line)}
.address-line{left:453px;width:189px;height:1px;background:var(--line)}
.back-contacts{left:29px;top:400px;color:var(--ink);font-size:13.2px;line-height:19.5px}
.back-contacts li{display:flex;align-items:center;gap:5px}
</style>
</head>
<body>

<section class="card front" aria-label="Postcard front">
  <svg class="card-bg" viewBox="0 0 1123 794" preserveAspectRatio="none" aria-hidden="true">
    <defs>
      <linearGradient id="accent" x1="0" y1="1" x2="1" y2="0">
        <stop offset="0" stop-color="#00a49b"/><stop offset="1" stop-color="#bfe9e4"/>
      </linearGradient>
    </defs>
    <polygon points="0,0 600,0 490,148 0,148" fill="#f3f5f7"/>
    <polygon points="600,0 1123,0 1123,72 545,72" fill="#00a49b"/>
    <polygon points="483,148 503,148 612,40 592,40" fill="url(#accent)"/>
    <rect x="0" y="354" width="1123" height="10" fill="#00a49b"/>
    <rect x="0" y="358" width="1123" height="350" fill="#0b72c6"/>
    <rect x="0" y="708" width="1123" height="86" fill="#00a49b"/>
  </svg>

  <div class="abs photo-forest" role="img" aria-label="Photo: children jumping and playing on the grass of a misty green forest"></div>

  <div class="abs brand">
    <span class="brand-dot"></span>
    <span class="brand-name">Bright Willow Kids</span>
  </div>
  <p class="abs brand-slogan">Improving skills and function for daily living</p>

  <p class="abs site-top">
    <svg width="13" height="13" viewBox="0 0 14 14" fill="none" stroke="#fff" stroke-width="1.1"><circle cx="7" cy="7" r="6"/><ellipse cx="7" cy="7" rx="2.6" ry="6"/><path d="M1 7h12M2 4h10M2 10h10"/></svg>
    <span>www.<b>brightwillowkids</b>.example</span>
  </p>

  <ul class="abs services">
    <li>Pediatric Occupational,</li>
    <li>Physical and Speech Therapy Services;</li>
    <li>Assistive Technology Evaluation and Training</li>
  </ul>

  <div class="abs pill">OCCUPATIONAL THERAPY</div>
  <p class="abs ot-intro">Our occupational therapists use play in therapy to help your child develop the skills he/she needs to perform their job of living and playing, including but not limited to:</p>
  <div class="abs rule-front"></div>

  <ul class="abs ot-list ot-left ticks">
    <li>Increasing independence in self-care skills such as feeding, dressing and grooming</li>
    <li>Improving developmental skills such as rolling, sitting, standing</li>
    <li>Improving their sensory processing, balance, coordination and motor planning</li>
    <li>Difficulty tolerating clothing</li>
    <li>Poor balance - doesn't ride a bike/climb on slides, falls frequently, cries when moved unexpectedly</li>
  </ul>
  <div class="abs divider-dots"></div>
  <ul class="abs ot-list ot-right ticks">
    <li>Intolerance to textures/odors/loud sounds/movement</li>
    <li>Delayed handwriting and fine motor skills and/or avoids fine motor activities such as using crayons, fasteners on clothing, pencils</li>
    <li>Limited diet-refuses to try new foods, gags when trying new tastes, textures</li>
    <li>Appears extremely anxious, states frequent fears of harmless things</li>
  </ul>

  <div class="abs cta-bar">CONTACT US TODAY FOR A FREE 15 MINUTE CONSULTATION/SCREEN</div>
  <div class="abs contact-row">
    <svg width="22" height="22" viewBox="0 0 24 24" fill="none" stroke="#fff" stroke-width="1.6"><circle cx="12" cy="12" r="10.5"/><path d="M8.3 6.5l2 2.4-1.1 1.6c.8 1.7 2.1 3 3.8 3.8l1.6-1.1 2.4 2-1.2 1.9c-4.4-.4-8.5-4.5-8.9-8.9z" fill="#fff" stroke="none"/></svg>
    <span>(301) 555-4182</span>
    <span class="sep"></span>
    <svg width="22" height="16" viewBox="0 0 24 17" fill="none" stroke="#fff" stroke-width="1.5"><rect x="1" y="1" width="22" height="15"/><path d="M1 1l11 9 11-9M1 16l8-7M23 16l-8-7"/></svg>
    <span>info@brightwillowkids.example</span>
  </div>
</section>

<section class="card back" aria-label="Postcard back">
  <svg class="card-bg" viewBox="0 0 1130 800" preserveAspectRatio="none" aria-hidden="true">
    <defs>
      <linearGradient id="goldband" x1="0" y1="0" x2="1" y2="0">
        <stop offset="0" stop-color="#f4d56a"/><stop offset="1" stop-color="#e6a65b"/>
      </linearGradient>
    </defs>
    <path d="M0,0 H645 C735,90 745,270 625,460 L545,600 V800 H668 C630,770 612,745 590,700 H0 Z" fill="#00a49b"/>
    <path d="M0,0 H565 C680,95 700,250 600,425 L548,520 L540,579 H0 Z" fill="#0b72c6" stroke="#fff" stroke-width="4"/>
    <path d="M0,579 H600 L640,800 H0 Z" fill="url(#goldband)"/>
    <circle cx="560" cy="607" r="153" fill="#00a49b"/>
  </svg>

  <svg class="abs photo-student" width="174" height="174" viewBox="0 0 174 174" role="img" aria-label="Photo: a boy in a red shirt writing in a notebook at a classroom desk">
    <defs>
      <radialGradient id="student" cx="50%" cy="45%" r="60%">
        <stop offset="0" stop-color="#8a6a55"/><stop offset=".6" stop-color="#a86450"/><stop offset="1" stop-color="#c9c2b8"/>
      </radialGradient>
    </defs>
    <circle cx="87" cy="87" r="86" fill="url(#student)"/>
  </svg>

  <h2 class="h-speech">SPEECH-LANGUAGE THERAPY</h2>
  <div class="abs back-rule" style="left:29px;top:49px;width:308px"></div>
  <ul class="abs speech-list ticks">
    <li>Oral Motor Skills</li><li>Voice</li><li>Speech Delays</li>
    <li>Language Skills</li><li>Fluency</li><li>Cognitive Skills</li>
    <li>Feeding Disorders</li><li>Articulation</li><li>Play Skills</li>
  </ul>

  <h2 class="h-physical">PHYSICAL THERAPY</h2>
  <div class="abs back-rule" style="left:29px;top:145px;width:298px"></div>
  <ul class="abs pt-list ticks">
    <li>Delayed crawling / walking<span class="col2 tick-item">Persistent toe walking habits</span></li>
    <li>Poor unsupported sitting/standing balance</li>
    <li>Trouble learning how to jump, skip, ride a bike</li>
    <li>Decreased ability to throw and catch a ball</li>
    <li>Delayed motor milestones<span class="col2 tick-item">Sports injuries</span></li>
    <li>Need for wheelchair mobility training</li>
    <li>Balance coordination and motor planning difficulty</li>
    <li style="width:230px">Strength , muscle tone and/ R range of motion impairment</li>
    <li style="width:200px">Postural control and positioning difficulty</li>
  </ul>

  <h2 class="h-contact">CONTACT US TODAY</h2>
  <div class="abs back-rule" style="left:29px;top:392px;width:217px;background:var(--ink)"></div>
  <ul class="abs back-contacts">
    <li><svg width="11" height="11" viewBox="0 0 24 24" fill="none" stroke="#2b2b2b" stroke-width="2"><circle cx="12" cy="12" r="10.5"/><path d="M8.3 6.5l2 2.4-1.1 1.6c.8 1.7 2.1 3 3.8 3.8l1.6-1.1 2.4 2-1.2 1.9c-4.4-.4-8.5-4.5-8.9-8.9z" fill="#2b2b2b" stroke="none"/></svg>(301) 555-4182</li>
    <li><svg width="11" height="8" viewBox="0 0 24 17" fill="none" stroke="#2b2b2b" stroke-width="2"><rect x="1" y="1" width="22" height="15"/><path d="M1 1l11 9 11-9"/></svg>info@brightwillowkids.example</li>
    <li><svg width="11" height="11" viewBox="0 0 14 14" fill="none" stroke="#2b2b2b" stroke-width="1.2"><circle cx="7" cy="7" r="6"/><ellipse cx="7" cy="7" rx="2.6" ry="6"/><path d="M1 7h12"/></svg>www.brightwillowkids.example</li>
  </ul>

  <div class="abs stamp"></div>
  <div class="abs address-line" style="top:247px"></div>
  <div class="abs address-line" style="top:284px"></div>
  <div class="abs address-line" style="top:320px"></div>
</section>

</body>
</html>
```